Student project platform needs an awareness flyer

Tornuvel is a matchmaking and crowdfunding site for student projects. On this platform, students can team up with each other to invent a new product, innovate, or start a business. They can also raise funds for their project.

** I am in need of an 8x11" flyer to print and distribute digitally which notifies students of all different skill sets that this site exists.

The flyer should communicate that a diverse user base is being built on this site, with people who have skills in programming, engineering, design, business, finance, and so on.

The flyer should also be clean and modern, with an emphasis on creativity and innovation. I've attached the business' logo to give you an idea of the artistic style we have already established.

Target Market(s)

University students

Industry/Entity Type

Crowdfunding

Font styles to use
Serif
Sans Serif

Requirements
Must have
• * Clean and modern design
• * Color scheme of my logo: #336699 and #669933 (blue and green)
• * Convey that this site is for people of different skill sets: programming, engineering, design, business, finance, and so on.
• * See the attached "Tornuvel Copy.txt" for text to include on the flyer

```html
<!DOCTYPE html>
<html lang="en">
<head>
<meta charset="utf-8">
<title>Tornuvel – Student Projects Flyer</title>
<link rel="stylesheet" href="https://fonts.googleapis.com/css2?family=Open+Sans:wdth,wght@75..100,400..800&family=PT+Sans:wght@400;700&display=swap">
<style>
  :root {
    --brand-blue: #336699;
    --brand-green: #669933;
    --ink: #1e1e1e;
    --muted: #3f3f3f;
    --paper: #ffffff;
    --stage: #e4e4e4;
    --photo-sky: #c9d6b5;
    --photo-deep: #7f8f5e;
    --photo-warm: #c8b692;
  }
  * { box-sizing: border-box; margin: 0; padding: 0; }
  html, body { width: 850px; height: 1200px; overflow: hidden; }
  body { background: var(--stage); position: relative; font-family: "PT Sans", Arial, sans-serif; }

  .flyer {
    position: absolute; left: 65px; top: 90px;
    width: 720px; height: 1020px;
    background: var(--paper);
    overflow: hidden;
    box-shadow: 0 6px 18px rgba(0,0,0,.25);
  }

  .hero { position: absolute; left: 0; top: 0; width: 720px; height: 420px; }
  .hero-photo {
    position: absolute; inset: 0;
    background: linear-gradient(180deg, var(--photo-sky) 0%, var(--photo-warm) 45%, var(--photo-deep) 100%);
  }
  .hero-wave { position: absolute; left: 0; top: 0; }

  .brand { position: absolute; left: 28px; top: 356px; width: 260px; }
  .brand-dot {
    width: 92px; height: 92px; border-radius: 50%;
    background: var(--brand-blue); margin-left: 62px;
  }
  .brand-name {
    margin-top: 24px;
    font-family: "Open Sans", Arial, sans-serif; font-weight: 400;
    font-size: 40px; letter-spacing: 1px; color: var(--brand-blue); line-height: 1;
  }

  .join { position: absolute; left: 26px; top: 532px; }
  .join-verb { font-size: 64px; font-weight: 700; color: var(--brand-green); line-height: 1; }
  .join-name { font-size: 48px; font-weight: 700; color: var(--brand-green); line-height: 1.05; letter-spacing: 1px; }
  .join-pitch { margin-top: 10px; font-family: Arial, "PT Sans", sans-serif; font-size: 25px; color: var(--muted); line-height: 33px; }
  .join-target { margin-top: 8px; font-size: 44px; font-weight: 700; color: var(--brand-blue); line-height: 48px; }

  .callout {
    position: absolute; right: 18px; top: 428px; text-align: right;
    font-family: "Open Sans", Arial, sans-serif; font-stretch: 75%; font-weight: 700;
  }
  .callout-head { font-size: 42px; color: var(--brand-blue); line-height: 46px; }
  .callout-sub { font-size: 26px; color: var(--brand-green); line-height: 26px; }
  .callout-goal { font-size: 40px; color: var(--ink); line-height: 44px; }
  .callout-goal.alt { color: var(--brand-blue); }
  .callout-goal .lead { color: var(--brand-green); }

  .about-tag {
    position: absolute; left: 384px; top: 598px; width: 336px; height: 48px;
    background: var(--brand-green); border-radius: 24px 0 0 24px;
    color: #fff; font-family: "Open Sans", Arial, sans-serif; font-weight: 700;
    font-size: 28px; line-height: 48px; padding-left: 22px;
  }
  .about-copy {
    position: absolute; right: 18px; top: 672px; width: 360px; text-align: right;
    white-space: nowrap;
    font-family: "Open Sans", Arial, sans-serif; font-size: 20px; line-height: 28px; color: var(--ink);
  }
  .about-copy .key { color: var(--brand-blue); }

  .skills {
    position: absolute; left: 0; top: 892px; width: 720px; height: 70px; list-style: none;
  }
  .skill {
    position: absolute; top: 0; width: 140px; margin-left: -70px; text-align: center;
    font-family: "Open Sans", Arial, sans-serif; font-weight: 700; font-size: 17px; color: var(--ink);
  }
  .skill svg { display: block; margin: 0 auto 6px; }

  .site-band {
    position: absolute; left: 0; bottom: 0; width: 720px; height: 40px;
    background: var(--brand-blue); color: #fff; text-align: center;
    font-family: "Open Sans", Arial, sans-serif; font-weight: 600; font-size: 25px; line-height: 40px;
  }
</style>
</head>
<body>
  <main class="flyer">
    <section class="hero">
      <div class="hero-photo" role="img" aria-label="Photo of five smiling university students outdoors in front of a campus building, stacking their hands together in the middle"></div>
      <svg class="hero-wave" width="720" height="420" viewBox="0 0 720 420" aria-hidden="true">
        <path d="M0,280 C80,285 160,330 250,338 C320,344 360,318 420,322 C470,326 480,372 540,372 C590,372 600,330 640,332 C680,334 700,380 720,395 L720,420 L0,420 Z" fill="var(--paper)"/>
        <path d="M0,280 C80,285 160,330 250,338 C320,344 360,318 420,322 C470,326 480,372 540,372 C590,372 600,330 640,332 C680,334 700,380 720,395" fill="none" stroke="var(--brand-blue)" stroke-width="8"/>
      </svg>
    </section>

    <div class="brand">
      <div class="brand-dot" aria-hidden="true"></div>
      <p class="brand-name">TORNUVEL</p>
    </div>

    <section class="join">
      <p class="join-verb">JOIN</p>
      <p class="join-name">TORNUVEL</p>
      <p class="join-pitch">TO SUPPORT AND<br>LEND YOUR<br>SKILLS TO</p>
      <p class="join-target">STUDENT<br>PROJECTS!</p>
    </section>

    <section class="callout">
      <p class="callout-head">Calling all students</p>
      <p class="callout-sub">who want to</p>
      <p class="callout-goal">Build, innovate, invent,</p>
      <p class="callout-goal alt"><span class="lead">or</span> start a business</p>
    </section>

    <h2 class="about-tag">What is Tornuvel?</h2>
    <p class="about-copy">Tornuvel is a matchmaking and<br>crowdfunding platform for<br>student projects. It allows<br>students to <span class="key">form teams</span> of<br>diverse skills and <span class="key">raise money</span><br>to build, innovate, invent,<br>or start a business.</p>

    <ul class="skills">
      <li class="skill" style="left:112px">
        <svg width="36" height="34" viewBox="0 0 36 34"><rect x="2" y="2" width="32" height="22" rx="2" fill="var(--brand-green)"/><rect x="7" y="8" width="14" height="2.5" fill="#fff"/><rect x="7" y="14" width="20" height="2.5" fill="#fff"/><rect x="14" y="26" width="8" height="4" fill="var(--brand-green)"/><rect x="9" y="30" width="18" height="3" fill="var(--brand-green)"/></svg>
        Programming
      </li>
      <li class="skill" style="left:259px">
        <svg width="36" height="34" viewBox="0 0 36 34" fill="none" stroke="var(--brand-green)" stroke-width="2.5"><rect x="9" y="8" width="18" height="18"/><rect x="14" y="13" width="8" height="8" fill="var(--brand-green)"/><path d="M13 8V3M18 8V3M23 8V3M13 26v5M18 26v5M23 26v5M9 12H4M9 17H4M9 22H4M27 12h5M27 17h5M27 22h5"/></svg>
        Engineering
      </li>
      <li class="skill" style="left:384px">
        <svg width="36" height="34" viewBox="0 0 36 34" fill="none" stroke="var(--brand-green)" stroke-width="2.5" stroke-linejoin="round"><path d="M18 3 33 10 18 17 3 10Z"/><path d="M3 17l15 7 15-7"/><path d="M3 24l15 7 15-7"/></svg>
        Design
      </li>
      <li class="skill" style="left:502px">
        <svg width="36" height="34" viewBox="0 0 36 34"><rect x="3" y="22" width="6" height="10" fill="var(--brand-green)"/><rect x="12" y="17" width="6" height="15" fill="var(--brand-green)"/><rect x="21" y="12" width="6" height="20" fill="var(--brand-green)"/><path d="M3 16 13 8l6 4 12-9" fill="none" stroke="var(--brand-green)" stroke-width="2.5"/><path d="M26 3h6v6" fill="none" stroke="var(--brand-green)" stroke-width="2.5"/></svg>
        Business
      </li>
      <li class="skill" style="left:622px">
        <svg width="36" height="34" viewBox="0 0 36 34"><circle cx="18" cy="13" r="11" fill="var(--brand-green)"/><text x="18" y="18" text-anchor="middle" font-family="Open Sans, Arial, sans-serif" font-weight="700" font-size="14" fill="#fff">$</text><path d="M4 31h28" stroke="var(--brand-green)" stroke-width="3"/></svg>
        Finance
      </li>
    </ul>

    <footer class="site-band">tornuvel.com</footer>
  </main>
</body>
</html>
```